Edible Insect Sticker packaging design

The successful designer for this product will be hired again for more packaging design products in this product range.
We are a company that manufactures edible insects and we have some new products coming out we ned packaging for. As you can imagine the stickers are very small 50mm x 50mm.
Each sticker design will be in a set  of 2 (one for the front and one for the back of the packaging).
The front will contain the weight of the product (in grams) as well as the name of the product and design.
The back will contain our company logo and info as well as NIP (Nutritional Information Panel), ingredient declaration, and 3-4 lines of information about how edible insects are great for the environment.
At this stage I would like the packaging to have a slightly environmental free, but still colourful and eye catching. I am open to any suggestions for the design though if you have some great ideas!
Must also contain the slogan (on front or back), "Are you Brave Enough?"
There are several products in the range, and would like the labels to be in a set. Basic lay out will be the same for each product, and the front sticker will be slightly different.
Products are
Zip-A-Dee Crumble- a fly shaped chocolate that contains coconut and fly pupae
Toasty Hoppers- 5 x roasted crickets
Nibbly Grublets- 5 x roasted mealworms
Cocoa Dipped Beasties- 5 x insects, chocolate coated in milk, white or dark chocolate. Insects include crickets, mealworms and fly pupae
Specific information (eg, NIP, ingredients etc) will be sent to chosen designer to add to the deisgn.
Attached is image of 3 products (Zip-A-Dee Crumble, roasted mealworms and roasted crickets) as well as logo. The chocolate coated bugs are the 2 types of roasted bugs pictured in the attachment coated in chocolate.

Updates
Design can be square or round 

Reason: Several designers have asked for an extension to submit new/ revised designs.

Reason: I have extended the deadline by one day to allow for revisions and new designs to be submitted.

Industry/Entity Type
It Company
Look and feel
Each slider illustrates characteristics of the customer's brand and the style your logo design should communicate.

```html
<!DOCTYPE html>
<html lang="en">
<head>
<meta charset="utf-8">
<title>Toasty Hoppers – Sticker Set</title>
<link href="https://fonts.googleapis.com/css2?family=Open+Sans:wght@400;700;800&family=PT+Sans:wght@400;700&display=swap" rel="stylesheet">
<style>
  :root {
    --bg: #f4f4f4;
    --olive: #7a7a2c;
    --olive-dark: #6b6a25;
    --leaf: #9cc43a;
    --leaf-pale: #edf4d9;
    --paper: #ffffff;
  }
  html, body {
    margin: 0;
    padding: 0;
    width: 1200px;
    height: 547px;
    overflow: hidden;
    background: var(--bg);
  }
  .canvas {
    position: relative;
    width: 1200px;
    height: 547px;
  }
  .sticker {
    position: absolute;
    top: 90px;
    width: 422px;
    height: 420px;
  }
  .sticker--front { left: 90px; }
  .sticker--back { left: 696px; }
  .sticker__shape {
    position: absolute;
    inset: 0;
  }
  .sticker__content {
    position: absolute;
    inset: 0;
    text-align: center;
    color: var(--olive);
  }
  .product-name {
    position: absolute;
    top: 72px;
    left: 0;
    right: 0;
    margin: 0;
    font-family: "Open Sans", sans-serif;
    font-weight: 700;
    font-size: 37px;
    letter-spacing: -0.3px;
  }
  .product-desc {
    position: absolute;
    top: 121px;
    left: 0;
    right: 0;
    margin: 0;
    font-family: "PT Sans", sans-serif;
    font-size: 21px;
  }
  .product-weight {
    position: absolute;
    top: 160px;
    left: 0;
    right: 0;
    margin: 0;
    font-family: "Open Sans", sans-serif;
    font-weight: 700;
    font-size: 21px;
    color: var(--leaf);
  }
  .brand {
    position: absolute;
    left: 0;
    right: 0;
    display: flex;
    justify-content: center;
    align-items: center;
    gap: 8px;
    font-family: "Open Sans", sans-serif;
    font-weight: 800;
    color: var(--olive);
  }
  .brand__dot {
    border-radius: 50%;
    background: var(--leaf);
    flex: none;
  }
  .brand--small { top: 228px; font-size: 22px; }
  .brand--small .brand__dot { width: 14px; height: 14px; }
  .brand--large { top: 100px; font-size: 38px; left: 40px; }
  .brand--large .brand__dot { width: 26px; height: 26px; }
  .slogan {
    position: absolute;
    top: 302px;
    left: 0;
    right: 0;
    margin: 0;
    font-family: "Open Sans", sans-serif;
    font-weight: 700;
    font-size: 19px;
    color: var(--olive);
  }
  .eco-info {
    position: absolute;
    top: 228px;
    left: 30px;
    right: 0;
    margin: 0;
    font-family: "PT Sans", sans-serif;
    font-size: 17.5px;
    line-height: 25px;
  }
  .nip {
    position: absolute;
    top: 310px;
    left: 30px;
    right: 0;
    margin: 0;
    font-family: "PT Sans", sans-serif;
    font-size: 16px;
  }
</style>
</head>
<body>
<main class="canvas">

  <section class="sticker sticker--front" aria-label="Front sticker">
    <svg class="sticker__shape" width="422" height="420" viewBox="0 0 422 420" aria-hidden="true">
      <defs>
        <clipPath id="front-inner">
          <path d="M24,58 Q211,26 398,58 L392,360 Q211,392 30,360 Z"/>
        </clipPath>
      </defs>
      <path d="M2,38 Q211,2 420,38 L412,382 Q211,416 10,382 Z" fill="var(--olive)"/>
      <path d="M12,47 Q211,13 410,47 L403,373 Q211,406 19,373 Z" fill="var(--paper)"/>
      <g clip-path="url(#front-inner)">
        <rect x="206" y="0" width="200" height="420" fill="var(--leaf-pale)" role="img" aria-label="Light green diagonal stripe texture"/>
      </g>
      <path d="M24,58 Q211,26 398,58 L392,360 Q211,392 30,360 Z" fill="none" stroke="var(--leaf)" stroke-width="3"/>
      <path d="M31,67 Q211,36 391,67 L385,351 Q211,382 37,351 Z" fill="none" stroke="var(--leaf)" stroke-width="2"/>
      <path class="ribbon-end" d="M46,306 L70,314 L70,330 L46,322 L54,314 Z" fill="var(--olive-dark)"/>
      <path class="ribbon-end" d="M366,306 L342,314 L342,330 L366,322 L358,314 Z" fill="var(--olive-dark)"/>
    </svg>
    <div class="sticker__content">
      <h1 class="product-name">Toasty Hoppers</h1>
      <p class="product-desc">5 roasted crickets</p>
      <p class="product-weight">xxx gr</p>
      <div class="brand brand--small"><span class="brand__dot"></span><span>Critter Pantry</span></div>
      <p class="slogan">Are you Brave Enough?</p>
    </div>
  </section>

  <section class="sticker sticker--back" aria-label="Back sticker">
    <svg class="sticker__shape" width="422" height="420" viewBox="0 0 422 420" aria-hidden="true">
      <defs>
        <clipPath id="back-inner">
          <path d="M24,58 Q211,26 398,58 L392,360 Q211,392 30,360 Z"/>
        </clipPath>
      </defs>
      <path d="M2,38 Q211,2 420,38 L412,382 Q211,416 10,382 Z" fill="var(--olive)"/>
      <path d="M12,47 Q211,13 410,47 L403,373 Q211,406 19,373 Z" fill="var(--paper)"/>
      <g clip-path="url(#back-inner)">
        <rect x="206" y="0" width="200" height="420" fill="var(--leaf-pale)" role="img" aria-label="Light green diagonal stripe texture"/>
      </g>
      <path d="M24,58 Q211,26 398,58 L392,360 Q211,392 30,360 Z" fill="none" stroke="var(--leaf)" stroke-width="3"/>
      <path d="M31,67 Q211,36 391,67 L385,351 Q211,382 37,351 Z" fill="none" stroke="var(--leaf)" stroke-width="2"/>
    </svg>
    <div class="sticker__content">
      <div class="brand brand--large"><span class="brand__dot"></span><span>Critter Pantry</span></div>
      <p class="eco-info">Information about how edible<br>insects are great for the environment</p>
      <p class="nip">NIP. 00000000000</p>
    </div>
  </section>

</main>
</body>
</html>
```